Web design for a pet services marketplace

I represent a South American based company: “TORVELIS” which provides a different array of pet related services. As a starting point, I would like to get proposals for 1 page website (plus a general frame for forms, instructions etc) web design job for a dog boarding marketplace. If you could add a logo is desirable.
By a Dog Boarding Marketplace, I mean a community marketplace, very much like an roomswap, but for pet services (initially dog boarding/daycare, but evolving to other services such as dog walkers. The purpose is to bring together dog owners and dog-care providers according to qualifications or characteristics given at time of input and needs of the dog owner given at the time of searching. Providers create a profile, entering certain information requested in forms such as their location, type of house/apt, what type/size of dogs they take, prior experience, as well as a personal introduction and pictures. Providers will set their own rates and calendar availability. Then customers browse, schedule and book and pay online. As it works for similar services, there will be a system of reviews and feedback for each care provider.
As to the website, it should be substantially similar to the following websites: (www.pupstayo.com , www.kelbo.com). It should be simple and straightforward, prioritizing ease of use. I would like for visitors to easily understand how the model works by seeing the home page, and getting pop up explanations by browsing over each main icon or message on the homepage. Therefore, I would try to keep additional pages to a minimum.
As I’m new to this, I would not venture as to how many pages I would need and would defer to your suggestion, according to the examples provided. However, I would like to have a visually striking front end, with dog related pictures or cartoon type images. Icons etc should be fun, and related to dogs, vacations, hotels/lodging, travel, etc. Secondary pages (like enrollment forms, Q&A, etc) could have a clean design, maybe adding some non-obtrusive related imagery.
Please note that attached pictures are , third party property and are for guide only.
Additional info:
In general I want to make a site very much like the examples of pupstayo and kelbo, but i think a better job could be done in terms of design. Please feel free to provide your own ideas.
1. For now, since the site will be new, we would not be including a testimonials section. However, we could use the space , or maybe smaller, with the "spread the love"section for announcing special deals for people who share the project.
2. In the principal section, I would like to see a clean layout. Much like pupstayo does. As an alternative, I would also like to see how it would look like if we handled more cartoon type drawings instead of pictures (just a suggestion to see how it would look like).
3. Search spaces should be more floating (merging more with background), as in pupstayo, not in larger boxes.
Updates
Please find in the attachments a very rough wire frame that i just did as response to a project proposal. Please note where i say OK (top and bottom) I mean that those two sections i found ok in such project or the model websites. Pretty regular content in those sections. Added Friday, July 10, 2015
Target Market(s)
dog owners, people who are willing to host pets in their home, kennels
Industry/Entity Type
Pet Care
Number of Pages Required
1 page
Look and feel

```html
<!DOCTYPE html>
<html lang="en">
<head>
<meta charset="utf-8">
<title>TORVELIS — Dog Boarding Marketplace</title>
<link rel="stylesheet" href="https://fonts.googleapis.com/css2?family=Open+Sans:wght@300;400;600;700&display=swap">
<style>
:root{
  --ink:#4a4a4a;
  --muted:#8a8a8a;
  --orange:#f0922b;
  --blue:#3aa9e0;
  --green:#7cc242;
  --cream:#f2eee2;
  --gray:#ececec;
  --footer-bar:#e2e2e2;
  --white:#ffffff;
}
*{box-sizing:border-box;margin:0;padding:0}
html,body{width:1200px;height:2708px;overflow:hidden}
body{font-family:"Open Sans",Arial,sans-serif;color:var(--ink);background:var(--white);position:relative}
.wrap{width:1200px;position:relative}

/* header */
.site-header{height:60px;display:flex;align-items:center;padding:0 40px 0 130px;background:var(--white);position:relative}
.brand{display:flex;align-items:center;gap:10px;font-weight:700;font-size:26px;color:#3b3b3b;letter-spacing:1px}
.brand-dot{width:26px;height:26px;border-radius:50%;background:var(--orange)}
.main-nav{display:flex;gap:30px;margin-left:40px;font-size:14px;color:var(--ink)}
.main-nav span{border-left:1px solid #ddd;padding-left:30px}
.main-nav span:first-child{border:0;padding-left:0}
.account{margin-left:auto;display:flex;align-items:center;gap:14px;font-size:14px}
.btn-outline{border:2px solid var(--orange);color:var(--ink);padding:8px 16px;border-radius:3px;font-size:14px}

/* hero */
.hero{height:540px;position:relative;background:linear-gradient(110deg,#7c8a86 0%,#a9b6b2 30%,#d9d6cc 55%,#c7b9a5 75%,#8e7a62 100%)}
.hero-copy{position:absolute;left:130px;top:70px;color:var(--white)}
.hero-copy h1{font-weight:300;font-size:44px}
.hero-copy p{font-size:14px;opacity:.9;margin-top:4px}
.search-row{position:absolute;left:130px;top:168px;display:flex}
.field{background:rgba(255,255,255,.92);height:40px;display:flex;align-items:center;gap:8px;padding:0 12px;font-size:13px;color:var(--muted)}
.field-city{width:370px}
.btn-green{background:var(--green);color:var(--white);height:40px;padding:0 24px;display:flex;align-items:center;font-weight:600;font-size:14px}
.search-row.second{top:216px;gap:8px}
.search-row.second .field{width:122px;height:34px}
.search-row.second .field.wide{width:130px}

/* welcome */
.welcome{background:var(--cream);height:230px;text-align:center;padding-top:28px}
.welcome h2{font-weight:300;font-size:34px}
.welcome h2 b{color:var(--orange);font-weight:700}
.welcome p{width:940px;margin:16px auto 0;font-size:12px;line-height:1.7;color:var(--muted)}
.btn-blue{display:inline-block;background:var(--blue);color:var(--white);padding:9px 22px;font-size:13px;border-radius:3px;margin-top:22px}

/* how it works */
.how{height:420px;text-align:center;padding-top:28px}
.how h2,.protect h2{font-weight:300;font-size:32px}
.how .sub{font-size:12px;color:var(--muted);margin-top:2px}
.steps{display:flex;justify-content:center;gap:150px;margin-top:110px}
.step{width:170px}
.step-icon{width:64px;height:64px;border-radius:4px;margin:0 auto;display:flex;align-items:center;justify-content:center}
.step h3{font-size:17px;font-weight:600;margin-top:14px}
.step p{font-size:11px;color:var(--muted);margin-top:4px;line-height:1.5}

/* protection */
.protect{background:var(--gray);height:480px;text-align:center;padding-top:36px}
.features{display:flex;justify-content:center;gap:120px;margin-top:50px}
.feature{width:210px}
.feature-img{height:170px;border-radius:4px}
.feature h3{font-size:18px;font-weight:600;margin-top:24px}
.feature p{font-size:11px;color:var(--muted);margin-top:6px;line-height:1.5}

/* spread */
.spread{height:465px;position:relative;background:linear-gradient(180deg,#5d6e3a 0%,#6f8a3c 40%,#5a7a2e 70%,#3f5a20 100%)}
.spread-copy{position:absolute;left:710px;top:155px;color:var(--white);width:340px}
.spread-copy h2{font-weight:300;font-size:40px}
.spread-copy p{font-size:12px;line-height:1.6;margin-top:8px;opacity:.9}
.btn-orange{display:inline-block;background:var(--orange);color:var(--white);padding:9px 20px;font-size:13px;border-radius:3px;margin-top:22px}

/* newsletter */
.newsletter{background:var(--cream);height:245px;text-align:center;padding-top:54px}
.newsletter h2{font-weight:400;font-size:24px}
.subscribe{display:flex;justify-content:center;gap:10px;margin-top:40px}
.subscribe .input{width:230px;height:36px;background:var(--white);border:1px solid #ddd;font-size:12px;color:var(--muted);display:flex;align-items:center;padding-left:12px}
.subscribe .btn{width:120px;height:36px;background:var(--blue);color:var(--white);font-size:13px;display:flex;align-items:center;justify-content:center}
.newsletter small{display:block;font-size:11px;color:var(--muted);margin-top:12px}

/* footer */
.site-footer{height:210px;display:flex;padding:40px 0 0 130px;gap:90px}
.footer-col h4{color:var(--orange);font-weight:400;font-size:22px;margin-bottom:12px}
.footer-col li{list-style:none;font-size:11px;line-height:1.8;color:var(--ink)}
.social{display:flex;gap:10px}
.social span{width:24px;height:24px;border-radius:50%;background:var(--blue)}
.footer-brand{margin-left:auto;margin-right:130px;margin-top:22px}
.copyright{background:var(--footer-bar);height:58px;display:flex;align-items:center;justify-content:center;font-size:11px;color:var(--muted)}
</style>
</head>
<body>
<div class="wrap">

<header class="site-header">
  <div class="brand"><span class="brand-dot"></span>TORVELIS</div>
  <nav class="main-nav"><span>Find a Sitter</span><span>How it Works</span></nav>
  <div class="account"><span>Log In</span><span>|</span><span>Sign Up</span><span class="btn-outline">Become a Sitter</span></div>
</header>

<section class="hero" role="img" aria-label="Photo of a smiling family of four hugging their golden labrador indoors">
  <div class="hero-copy">
    <h1>Find a Loving Dog Sitter</h1>
    <p>Search thousands of trusted, reviewed pet sitters near you</p>
  </div>
  <div class="search-row">
    <div class="field field-city">
      <svg width="12" height="14" viewBox="0 0 12 14"><path d="M6 0a5 5 0 0 0-5 5c0 4 5 9 5 9s5-5 5-9a5 5 0 0 0-5-5zm0 7a2 2 0 1 1 0-4 2 2 0 0 1 0 4z" fill="#999"/></svg>
      Enter a city</div>
    <div class="btn-green">Find a Sitter</div>
  </div>
  <div class="search-row second">
    <div class="field"><svg width="12" height="12"><circle cx="6" cy="6" r="5" fill="none" stroke="#999"/></svg>Overnight</div>
    <div class="field wide"><svg width="12" height="12"><rect x="1" y="2" width="10" height="9" fill="none" stroke="#999"/></svg>Start Date</div>
    <div class="field wide"><svg width="12" height="12"><rect x="1" y="2" width="10" height="9" fill="none" stroke="#999"/></svg>End Date</div>
  </div>
</section>

<section class="welcome">
  <h2>Welcome to <b>TORVELIS</b></h2>
  <p>Our community connects dog owners with caring local hosts who treat every guest like family. Browse detailed profiles, compare rates and availability, read honest reviews from other owners and book a stay in a few simple steps. Whether you need a weekend sitter or daily care, you will find a cosy home away from home for your best friend.</p>
  <span class="btn-blue">Read More</span>
</section>

<section class="how">
  <h2>How It Works</h2>
  <p class="sub">Three easy steps to a happy dog</p>
  <div class="steps">
    <div class="step">
      <div class="step-icon" style="background:var(--orange)"><svg width="30" height="30" viewBox="0 0 30 30"><circle cx="12" cy="12" r="8" fill="none" stroke="#fff" stroke-width="3"/><line x1="18" y1="18" x2="27" y2="27" stroke="#fff" stroke-width="4"/></svg></div>
      <h3>Search Sitters</h3>
      <p>Browse loving, trusted dog sitters near you</p>
    </div>
    <div class="step">
      <div class="step-icon" style="background:var(--blue)"><svg width="30" height="30" viewBox="0 0 30 30"><rect x="4" y="6" width="22" height="20" rx="2" fill="none" stroke="#fff" stroke-width="3"/><line x1="4" y1="12" x2="26" y2="12" stroke="#fff" stroke-width="3"/></svg></div>
      <h3>Book Online</h3>
      <p>Choose dates and pay securely in minutes</p>
    </div>
    <div class="step">
      <div class="step-icon" style="background:var(--green)"><svg width="30" height="30" viewBox="0 0 30 30"><path d="M6 16l6 6 12-14" fill="none" stroke="#fff" stroke-width="4"/></svg></div>
      <h3>Relax</h3>
      <p>Enjoy your trip while your dog is spoiled</p>
    </div>
  </div>
</section>

<section class="protect">
  <h2>Book through Kelbo and Enjoy Peace of Mind Protection</h2>
  <div class="features">
    <div class="feature">
      <div class="feature-img" role="img" aria-label="Photo of a puppy sitting on a white background" style="background:linear-gradient(180deg,#f6f2ea,#d9b98a)"></div>
      <h3>Insured Pets</h3>
      <p>Every booking includes premium care cover for your dog.</p>
    </div>
    <div class="feature">
      <div class="feature-img" role="img" aria-label="Photo of a yellow puppy looking through a magnifying glass" style="background:linear-gradient(180deg,#f4efe6,#d8b27a)"></div>
      <h3>Vetted Hosts</h3>
      <p>All hosts pass profile checks before they can accept guests.</p>
    </div>
    <div class="feature">
      <div class="feature-img" role="img" aria-label="Photo of a family relaxing on the floor with their dog" style="background:linear-gradient(180deg,#eef0f3,#b7a48a)"></div>
      <h3>One on One TLC</h3>
      <p>Your dog gets personal attention in a real home setting.</p>
    </div>
  </div>
</section>

<section class="spread" role="img" aria-label="Photo of a happy dog running across green grass">
  <div class="spread-copy">
    <h2>Love the spread</h2>
    <p>Share our community with friends and unlock special deals on your next booking.</p>
    <span class="btn-orange">Become a Sitter</span>
  </div>
</section>

<section class="newsletter">
  <h2>Stay in Touch with PupStayo for the Latest Dog Tips</h2>
  <div class="subscribe">
    <div class="input">Your Name</div>
    <div class="input">Your Email</div>
    <div class="btn">Subscribe</div>
  </div>
  <small>Hey, you just might get some nice puppy photos too!</small>
</section>

<footer class="site-footer">
  <div class="footer-col"><h4>Company</h4><ul><li>About us</li><li>Terms of service</li><li>Privacy Policy</li></ul></div>
  <div class="footer-col"><h4>Help</h4><ul><li>Support Center</li><li>How booking works</li><li>Contact us</li></ul></div>
  <div class="footer-col"><h4>Follow us</h4><div class="social"><span></span><span></span><span></span><span></span><span></span></div></div>
  <div class="brand footer-brand"><span class="brand-dot"></span>TORVELIS</div>
</footer>
<div class="copyright">Copyright © 2015 - TORVELIS - All Rights Reserved</div>

</div>
</body>
</html>
```